Darrow Consulting needs a quality & professional business card!

I am a recruitment and employment consultant from Brisbane, Australia and I had a fantastic logo organised by this community to I am hoping the business card will be the same.

I have attached the Darrow consulting logo that ideally would feature on the back of the business card. There are a number of logos for you to use as you see fit. I would like the colour cheme to match that of the Darrow Consulting logo. I also have a secondary company called Career Lantern Australia and I have included that logo as well. While it is an important part of the business I don't want this logo feature too predominantly as I am moving out of this space. This logo was created by myself and is of low quality. Feel free to use the icon and words however you want. The winning design will be smart, professional and eye-catching.

The information I am looking for in the business card is:
Name: Gavin Darrow
Position: Founder & Director
Phone: (07) 3519 6482
Mobile: 0431 586 207
Email: gavin@careerlantern.com.au

Target Market(s)

Recruiters, government, large companies

Contact Information for Business Card

Name: Gavin Darrow
Phone: (07) 3519 6482
Mobile: 0431 586 207
Web: www.careerlantern.com.au

Font styles to use
Serif
Sans Serif

Requirements
Must have
• Darrow Consulting Logo on reverse side
• Contact details on front side with smaller reference to Darrow Consulting logo and Career Lantern Australia logo

```html
<!DOCTYPE html>
<html lang="en">
<head>
<meta charset="utf-8">
<title>Darrow Consulting – Business Card</title>
<link rel="stylesheet" href="https://fonts.googleapis.com/css2?family=Montserrat:wght@400;500;700&display=swap">
<style>
  :root {
    --stage: #e4e4e4;
    --card-white: #ffffff;
    --charcoal: #1e2022;
    --charcoal-back: #25282a;
    --orange: #e0832f;
    --ink: #1a1a1a;
    --logo-grey: #c9c9c9;
  }
  html, body {
    margin: 0;
    padding: 0;
    width: 1200px;
    height: 1000px;
    overflow: hidden;
    background: var(--stage);
    font-family: "Montserrat", Arial, sans-serif;
  }
  .canvas {
    position: relative;
    width: 1200px;
    height: 1000px;
  }
  .card {
    position: absolute;
    overflow: hidden;
  }
  .card-front {
    left: 66px;
    top: 57px;
    width: 698px;
    height: 419px;
    background: var(--card-white);
  }
  .front-shapes {
    position: absolute;
    inset: 0;
  }
  .front-brand {
    position: absolute;
    left: 50px;
    top: 246px;
    display: flex;
    align-items: center;
    gap: 14px;
  }
  .brand-dot {
    width: 16px;
    height: 16px;
    border-radius: 50%;
    background: var(--charcoal);
  }
  .brand-name {
    font-weight: 500;
    font-size: 27px;
    line-height: 1.05;
    letter-spacing: 2px;
    text-transform: uppercase;
    color: var(--charcoal);
  }
  .holder {
    position: absolute;
    right: 48px;
    top: 63px;
    text-align: right;
  }
  .holder-name {
    margin: 0;
    font-weight: 700;
    font-size: 22px;
    letter-spacing: 0.5px;
    color: var(--orange);
    text-transform: uppercase;
  }
  .holder-role {
    margin: 3px 0 0;
    font-weight: 500;
    font-size: 14.5px;
    color: var(--ink);
  }
  .contacts {
    position: absolute;
    right: 48px;
    top: 232px;
    margin: 0;
    padding: 0;
    list-style: none;
    text-align: right;
  }
  .contacts li {
    display: flex;
    justify-content: flex-end;
    align-items: center;
    gap: 5px;
    font-size: 14.5px;
    font-weight: 500;
    color: var(--ink);
    height: 21px;
  }
  .contacts svg {
    width: 11px;
    height: 11px;
    flex: none;
  }
  .partner {
    position: absolute;
    right: 48px;
    top: 354px;
    display: flex;
    align-items: center;
    gap: 7px;
  }
  .partner-square {
    width: 22px;
    height: 22px;
    background: var(--ink);
    border-radius: 3px;
  }
  .partner-name {
    font-weight: 500;
    font-size: 13px;
    line-height: 1.1;
    color: var(--ink);
  }
  .card-back {
    left: 401px;
    top: 525px;
    width: 696px;
    height: 416px;
    background: var(--charcoal-back);
  }
  .back-brand {
    position: absolute;
    left: 0;
    right: 0;
    top: 0;
    bottom: 0;
    display: flex;
    align-items: center;
    justify-content: center;
    gap: 24px;
  }
  .back-brand .brand-dot {
    width: 30px;
    height: 30px;
    background: var(--logo-grey);
  }
  .back-brand .brand-name {
    font-size: 44px;
    letter-spacing: 4px;
    color: var(--logo-grey);
  }
</style>
</head>
<body>
<main class="canvas">

  <section class="card card-front" aria-label="Business card front">
    <svg class="front-shapes" width="698" height="419" viewBox="0 0 698 419" aria-hidden="true">
      <polygon points="0,0 432,0 286,206 0,206" fill="var(--charcoal)"/>
      <polygon points="432,0 446,0 300,206 286,206" fill="var(--orange)"/>
      <polygon points="0,351 196,351 160,419 0,419" fill="var(--orange)"/>
    </svg>

    <div class="front-brand">
      <span class="brand-dot"></span>
      <span class="brand-name">Darrow<br>Consulting</span>
    </div>

    <header class="holder">
      <h1 class="holder-name">Gavin Darrow</h1>
      <p class="holder-role">Founder &amp; Director</p>
    </header>

    <ul class="contacts">
      <li>(07) 3519 6482
        <svg viewBox="0 0 12 12" aria-hidden="true"><path d="M2.5 1 L4.5 1 L5.3 3.6 L4 4.6 Q5 7 7.4 8 L8.4 6.7 L11 7.5 L11 9.5 Q10.5 11 9 11 Q1 10.5 1 3 Q1 1.5 2.5 1 Z" fill="var(--orange)"/></svg>
      </li>
      <li>0431 586 207
        <svg viewBox="0 0 12 12" aria-hidden="true"><rect x="3" y="0.5" width="6" height="11" rx="1" fill="none" stroke="var(--orange)" stroke-width="1.2"/><circle cx="6" cy="9.6" r="0.7" fill="var(--orange)"/></svg>
      </li>
      <li>gavin@careerlantern.com.au
        <svg viewBox="0 0 12 12" aria-hidden="true"><rect x="0.8" y="2.5" width="10.4" height="7.5" fill="var(--orange)"/><path d="M0.8 2.5 L6 6.8 L11.2 2.5" fill="none" stroke="#fff" stroke-width="1"/></svg>
      </li>
      <li>www.careerlantern.com.au
        <svg viewBox="0 0 12 12" aria-hidden="true"><circle cx="6" cy="6" r="5" fill="none" stroke="var(--orange)" stroke-width="1.2"/><ellipse cx="6" cy="6" rx="2.2" ry="5" fill="none" stroke="var(--orange)" stroke-width="1"/><line x1="1" y1="6" x2="11" y2="6" stroke="var(--orange)" stroke-width="1"/></svg>
      </li>
    </ul>

    <div class="partner">
      <span class="partner-square"></span>
      <span class="partner-name">Career Lantern<br>Australia</span>
    </div>
  </section>

  <section class="card card-back" aria-label="Business card back">
    <div class="back-brand">
      <span class="brand-dot"></span>
      <span class="brand-name">Darrow<br>Consulting</span>
    </div>
  </section>

</main>
</body>
</html>
```